Modern Design Business Card industrial maintenance company

Business card design for Company named Brookvale Equipment Services

Target Market(s)

Industrial

Industry/Entity Type

Maintenance and repair

Contact Information for Business Card

Place holder for address, office phone, mobile number and email

Requirements
Must have
• Clean modern look
Nice to have
• N/a

```html
<!DOCTYPE html>
<html lang="en">
<head>
<meta charset="utf-8">
<title>Brookvale Equipment Services – Business Card</title>
<link href="https://fonts.googleapis.com/css2?family=Poppins:wght@400;600&display=swap" rel="stylesheet">
<style>
  :root {
    --backdrop: #d6cbbd;
    --card-light: #e9e2d8;
    --card-edge: #f4efe8;
    --ink-dark: #1c1a19;
    --band-dark: #201d1c;
    --band-mid: #2e2a29;
    --gold: #d9c7ad;
    --gold-soft: #c9b597;
  }
  * { margin: 0; padding: 0; box-sizing: border-box; }
  html, body {
    width: 1200px; height: 1046px; overflow: hidden;
    background: var(--backdrop);
    font-family: "Poppins", sans-serif;
  }
  .canvas { position: relative; width: 1200px; height: 1046px; }
  .card {
    position: absolute; left: 60px; top: 230px;
    width: 1080px; height: 586px;
    border-radius: 30px; overflow: hidden;
    background: var(--card-light);
    box-shadow: 0 0 0 2px var(--card-edge), 0 20px 50px rgba(60,45,30,.25);
  }
  .card-panel { position: absolute; inset: 0; }
  .brand {
    position: absolute; left: 40px; top: 40px; width: 386px;
    text-align: center; color: var(--ink-dark);
  }
  .brand-mark {
    width: 120px; height: 120px; margin: 0 auto 18px;
    border: 6px solid var(--ink-dark); border-radius: 50%;
  }
  .brand-name {
    font-weight: 600; font-size: 27px; line-height: 1.2; letter-spacing: 1px;
    text-transform: uppercase;
  }
  .contact {
    position: absolute; right: 43px; top: 238px;
    text-align: right; color: var(--gold);
  }
  .person-name { font-size: 40px; line-height: 1.1; font-weight: 400; }
  .person-name strong { font-weight: 600; }
  .person-title { font-size: 22px; margin-top: 8px; }
  .address { font-size: 21px; line-height: 31px; margin-top: 26px; }
  .lines { list-style: none; margin-top: 26px; font-size: 22px; line-height: 32px; }
  .lines li { display: flex; justify-content: flex-end; align-items: center; gap: 16px; }
  .lines svg { width: 22px; height: 22px; flex: none; }
</style>
</head>
<body>
<div class="canvas">
  <div class="card">
    <svg class="card-panel" viewBox="0 0 1080 586" aria-hidden="true">
      <defs>
        <linearGradient id="panel" x1="0" y1="0" x2="1" y2="0">
          <stop offset="0" stop-color="var(--band-dark)"/>
          <stop offset=".45" stop-color="var(--band-mid)"/>
          <stop offset="1" stop-color="var(--band-dark)"/>
        </linearGradient>
      </defs>
      <polygon points="0,420 1080,110 1080,586 0,586" fill="url(#panel)"/>
      <line x1="0" y1="404" x2="1080" y2="94" stroke="var(--gold-soft)" stroke-width="4"/>
    </svg>

    <div class="brand">
      <div class="brand-mark"></div>
      <div class="brand-name">Brookvale Equipment Services</div>
    </div>

    <div class="contact">
      <h1 class="person-name"><strong>Marta</strong> Novakova</h1>
      <p class="person-title">Co-Founder &amp; CEO</p>
      <p class="address">1840 Ridgeline Ave. Suite 310<br>Arlington, TX 76011</p>
      <ul class="lines">
        <li>(817) 555-0143
          <svg viewBox="0 0 24 24"><path d="M6.6 10.8a15 15 0 0 0 6.6 6.6l2.2-2.2a1 1 0 0 1 1-.25 11.4 11.4 0 0 0 3.6.57 1 1 0 0 1 1 1V20a1 1 0 0 1-1 1A17 17 0 0 1 3 4a1 1 0 0 1 1-1h3.5a1 1 0 0 1 1 1c0 1.25.2 2.45.57 3.57a1 1 0 0 1-.25 1z" fill="var(--gold)"/></svg>
        </li>
        <li>(555) 010-2758
          <svg viewBox="0 0 24 24"><rect x="6" y="2" width="12" height="20" rx="2" fill="none" stroke="var(--gold)" stroke-width="2"/><circle cx="12" cy="18" r="1.2" fill="var(--gold)"/></svg>
        </li>
        <li>www.website.com
          <svg viewBox="0 0 24 24"><circle cx="12" cy="12" r="9" fill="none" stroke="var(--gold)" stroke-width="2"/><path d="M3 12h18M12 3c3 3 3 15 0 18M12 3c-3 3-3 15 0 18" fill="none" stroke="var(--gold)" stroke-width="1.5"/></svg>
        </li>
        <li>info@website.com
          <svg viewBox="0 0 24 24"><rect x="3" y="6" width="18" height="13" rx="1.5" fill="none" stroke="var(--gold)" stroke-width="2"/><path d="M3 7l9 7 9-7" fill="none" stroke="var(--gold)" stroke-width="2"/></svg>
        </li>
      </ul>
    </div>
  </div>
</div>
</body>
</html>
```